Norquel Cardiac Technologies

There is three component of my company
1- device ( heart Monitoring) and related software sales and Marketing
2- we do 24 hrs and 7 days of live streaming monitoring and provide daily and end of study reports to doctors
3- we also provide software and Rhythm interpretation training
Updates

Target Market(s)

hospitals and other small facilities . Technology itself called MCOT ( mobile Cardiac outpatient telemetry .

Industry/Entity Type

Healthcare

Font styles to use
Sans Serif

Requirements
Must have
• Refrences..
• Caldexa technologies.
• - quorvandixa ( taplor)
• - brovaline
• - dune harbor
Nice to have
• Refrences..
• -Caldexa technologies.
• - brovaline
• - dune harbor
Should not have
• Refrences..
• -Caldexa technologies.
• - brovaline
• - dune harbor

```html
<!DOCTYPE html>
<html lang="en">
<head>
<meta charset="utf-8">
<title>Norquel Cardiac Technologies – Brochure</title>
<link href="https://fonts.googleapis.com/css2?family=Oswald:wght@400;500;600&family=Roboto+Condensed:wght@400;700&display=swap" rel="stylesheet">
<style>
:root{
  --blue:#2f6db5;
  --blue-dark:#1d4c8c;
  --blue-light:#dfe9f6;
  --panel:#ffffff;
  --panel-alt:#f1f4f8;
  --ink:#2a3340;
  --red:#d8282f;
  --ecg-bg:#f6f8fb;
  --ecg-line:#b9c7da;
  --stage:#e8eaed;
}
*{box-sizing:border-box;margin:0;padding:0}
html,body{width:1200px;height:800px;overflow:hidden}
body{background:var(--stage);font-family:"Roboto Condensed",Arial,sans-serif;color:var(--ink);position:relative}
.strip{position:absolute;left:30px;width:1140px;height:350px;display:flex;box-shadow:0 2px 6px rgba(0,0,0,.12)}
.strip--outside{top:28px}
.strip--inside{top:420px}
.panel{position:relative;height:100%;background:var(--panel);border-top:10px solid var(--blue);border-bottom:10px solid var(--blue);padding:10px 10px 8px;overflow:hidden}
.strip--outside .panel{width:190px}
.strip--inside .panel{width:175px}
.panel--alt{background:var(--panel-alt)}
.panel + .panel{border-left:1px solid #d5dbe3}
.heading{font-family:"Oswald",Arial,sans-serif;font-weight:500;font-size:11px;letter-spacing:.3px;color:var(--blue);text-transform:uppercase;text-align:center;line-height:1.2}
.subheading{font-size:5.5px;color:var(--blue);text-align:center;text-transform:uppercase;margin-top:2px}
.band{background:var(--blue);color:#fff;font-family:"Oswald",Arial,sans-serif;font-size:10px;text-transform:uppercase;text-align:center;padding:4px 4px;margin:0 -10px}
.pill{display:inline-block;background:var(--blue);color:#fff;font-family:"Oswald",Arial,sans-serif;font-size:9px;text-transform:uppercase;padding:3px 10px;border-radius:0 10px 10px 0}
.bullets{list-style:none;margin-top:8px}
.bullets li{font-size:6.4px;line-height:1.35;color:var(--blue);text-transform:uppercase;margin-bottom:5px}
.bullets li::before{content:"– "}
.wordmark{display:flex;align-items:center;gap:4px;font-family:"Roboto Condensed",Arial,sans-serif;font-weight:700;font-size:10px;color:var(--red);line-height:1.1}
.wordmark i{width:9px;height:9px;border-radius:50%;background:var(--red);flex:none}
.wordmark--small{font-size:8px}
.wordmark--small i{width:7px;height:7px}
.figure{border:1px solid var(--ecg-line);background:linear-gradient(180deg,var(--ecg-bg),#e4ebf4)}
.figure--dark{background:linear-gradient(160deg,#2a3442,#11161d);border:none}
.figure--screen{background:linear-gradient(180deg,#1f3b66,#0f2240);border:none}
.figure--skin{background:linear-gradient(180deg,#d7b49a,#b98d70)}
/* tables */
.compare{width:100%;border-collapse:collapse;table-layout:fixed;font-size:4.6px;color:var(--ink)}
.compare th{background:var(--blue);color:#fff;font-weight:700;padding:2px 1px;line-height:1.1;overflow-wrap:anywhere}
.compare td{border:1px solid #c9d3e0;padding:2px 1px;text-align:center;line-height:1.15;overflow-wrap:anywhere}
.compare td:first-child{text-align:left;font-weight:700}
.compare tr:nth-child(even) td{background:#eef3f9}
.compare--narrow{font-size:3.9px}
.compare--narrow th,.compare--narrow td{padding:2px .5px}
.compare--narrow col.label{width:24px}
/* outside panels */
.cover-contact{margin-top:6px;background:var(--blue);color:#fff;font-family:"Oswald",Arial,sans-serif;font-size:6.5px;text-align:center;padding:3px}
.contact-lines{font-size:5.6px;color:var(--blue);text-align:center;line-height:1.7;margin-top:4px;text-transform:uppercase;white-space:nowrap}
.split{display:flex;gap:4px;margin-top:8px}
.split-left{width:58px;flex:none;padding-top:70px}
.split-right{flex:1;min-width:0}
.report{margin-top:8px;height:140px;background:#fbf7d8;border:1px solid #cfc68a;padding:4px;font-size:4.8px}
.report-row{display:flex;justify-content:space-between;border-bottom:1px solid #e2d99b;padding:2px 0}
.report-title{background:#1f2a36;color:#fff;text-align:center;font-size:5px;padding:2px;margin-bottom:3px}
.cover-top{display:flex;justify-content:center;padding:6px 0 8px}
.cover-body{display:flex;gap:6px;margin-top:6px}
.cover-body .figure{width:70px;height:150px;flex:none}
.cover-text{font-size:5.6px;color:var(--blue);text-transform:uppercase;line-height:1.35}
.cover-text ul{list-style:none;margin-top:4px}
.cover-text li{margin-bottom:2px}
.cover-text li::before{content:"– "}
.cover-sub{font-family:"Oswald",Arial,sans-serif;font-size:7px;color:var(--blue);text-align:center;margin:5px 0 2px;text-transform:uppercase}
.leads-tag{font-family:"Oswald",Arial,sans-serif;font-size:6.5px;color:var(--blue);text-transform:uppercase;margin-top:5px}
/* inside panels */
.sidebar{width:90px;height:100%;background:var(--blue-dark);color:#fff;padding:24px 8px;position:relative;border-top:10px solid var(--blue);border-bottom:10px solid var(--blue)}
.sidebar-title{font-family:"Oswald",Arial,sans-serif;font-size:7.5px;text-transform:uppercase;margin-bottom:6px}
.sidebar ul{list-style:none;font-size:5.8px;line-height:1.4;text-transform:uppercase}
.sidebar li{margin-bottom:4px}
.sidebar li::before{content:"– "}
.sidebar-contact{position:absolute;left:8px;right:8px;bottom:24px;font-size:5.8px;line-height:1.6;text-transform:uppercase}
.body-copy{font-size:6px;color:var(--blue);text-transform:uppercase;line-height:1.4;margin-top:6px}
.body-copy p{margin-bottom:4px}
.chest{position:relative;margin-top:6px;height:140px}
.chest .figure{position:absolute;left:0;top:0;width:84px;height:140px}
.lead-list{position:absolute;right:0;top:6px;width:64px;font-size:6px;color:var(--blue);line-height:1.5;text-transform:uppercase}
.stack{display:flex;flex-direction:column;gap:6px}
.lead-card .band{margin:0 0 4px}
</style>
</head>
<body>

<section class="strip strip--outside" aria-label="Brochure outside">

  <article class="panel">
    <h2 class="heading">Competitive Comparisons</h2>
    <p class="subheading">Data is informed by Norquel, we will make any appropriate changes</p>
    <div class="split">
      <div class="split-left">
        <div class="wordmark wordmark--small"><i></i><span>Norquel Cardiac Technologies</span></div>
        <div class="cover-contact">Contact Information</div>
        <div class="contact-lines">Office: (555) 014-2280<br>Toll free: (800) 555-0147<br>Fax: (555) 014-2291</div>
      </div>
      <div class="split-right">
        <table class="compare compare--narrow">
          <colgroup><col class="label"><col><col><col><col><col></colgroup>
          <tr><th></th><th>Norquel</th><th>Caldexa</th><th>quorvan­dixa (taplor)</th><th>brova­line</th><th>dune harbor</th></tr>
          <tr><td>Real-time ECG</td><td>●</td><td>–</td><td>●</td><td>–</td><td>●</td></tr>
          <tr><td>Wi-Fi unit</td><td>●</td><td>–</td><td>–</td><td>–</td><td>–</td></tr>
          <tr><td>Six leads</td><td>●</td><td>–</td><td>–</td><td>●</td><td>–</td></tr>
          <tr><td>Full disclosure</td><td>●</td><td>●</td><td>●</td><td>–</td><td>●</td></tr>
          <tr><td>A-fib burden</td><td>●</td><td>●</td><td>●</td><td>●</td><td>–</td></tr>
          <tr><td>QTc</td><td>●</td><td>–</td><td>–</td><td>–</td><td>–</td></tr>
          <tr><td>TWA</td><td>●</td><td>–</td><td>–</td><td>–</td><td>–</td></tr>
          <tr><td>72 h battery</td><td>●</td><td>●</td><td>–</td><td>●</td><td>●</td></tr>
        </table>
      </div>
    </div>
  </article>

  <article class="panel panel--alt">
    <h2 class="heading">Competitive Comparisons</h2>
    <p class="subheading">Real-time different cardiac telemetry</p>
    <table class="compare" style="margin-top:10px">
      <colgroup><col style="width:38px"><col><col><col><col><col></colgroup>
      <tr><th></th><th>Norquel</th><th>Caldexa</th><th>quorvan­dixa (taplor)</th><th>brova­line</th><th>dune harbor</th></tr>
      <tr><td>Live streaming</td><td>●</td><td>●</td><td>●</td><td>–</td><td>●</td></tr>
      <tr><td>Daily reports</td><td>●</td><td>●</td><td>●</td><td>●</td><td>●</td></tr>
      <tr><td>End reports</td><td>●</td><td>●</td><td>●</td><td>●</td><td>●</td></tr>
      <tr><td>Patch option</td><td>●</td><td>●</td><td>–</td><td>–</td><td>–</td></tr>
      <tr><td>Hospital use</td><td>●</td><td>–</td><td>–</td><td>–</td><td>–</td></tr>
      <tr><td>Holter file</td><td>●</td><td>–</td><td>●</td><td>–</td><td>–</td></tr>
      <tr><td>Rhythm training</td><td>●</td><td>–</td><td>–</td><td>–</td><td>–</td></tr>
    </table>
  </article>

  <article class="panel">
    <div class="report">
      <div class="report-title">Study Summary</div>
      <div class="report-row"><span>Patient</span><span>—</span></div>
      <div class="report-row"><span>Study date</span><span>—</span></div>
      <div class="report-row"><span>Heart rate</span><span>—</span></div>
      <div class="report-row"><span>A-fib burden</span><span>—</span></div>
      <div class="report-row"><span>Longest episode</span><span>—</span></div>
      <div class="report-row"><span>Findings</span><span>—</span></div>
    </div>
    <ul class="bullets">
      <li>Reports are delivered daily and at the end of each study.</li>
      <li>Summary data is reviewed by a certified technician.</li>
    </ul>
  </article>

  <article class="panel panel--alt">
    <h2 class="heading">The Very Best in Atrial Fib</h2>
    <div class="figure" style="height:120px;margin-top:8px" role="img" aria-label="Atrial fibrillation ECG trend and strip screenshot"></div>
    <ul class="bullets">
      <li>A-fib detection is found in both the real-time ECG trends and the Holter processing.</li>
      <li>The A-fib identification and coding are excellent, the best available.</li>
      <li>A-fib burden is provided.</li>
      <li>A unique time display shows the length of each A-fib event.</li>
    </ul>
  </article>

  <article class="panel">
    <h2 class="heading">Elongated QTc</h2>
    <div class="figure" style="height:120px;margin-top:8px" role="img" aria-label="ECG strip with QTc measurement ruler"></div>
    <ul class="bullets">
      <li>QTc analysis is provided for all ECG complexes during the monitoring time period.</li>
      <li>Finding the elongated QTc is a simple and quick process.</li>
      <li>An electronic ruler is provided for verification of the data.</li>
      <li>The yellow arrow is the 96% of R-R.</li>
    </ul>
  </article>

  <article class="panel panel--alt">
    <div class="cover-top"><div class="wordmark"><i></i><span>Norquel Cardiac Technologies</span></div></div>
    <div class="band">Knowledge, Experience, Quality</div>
    <p class="cover-sub">NQ-7 Wi-Fi Transmitter</p>
    <div class="cover-body">
      <div class="figure figure--dark" role="img" aria-label="Handheld Wi-Fi ECG transmitter device with screen"></div>
      <div class="cover-text">
        <p>Major breakthrough in long term ECG recordings. The NQ-7 cardiac monitoring software is a major step forward.</p>
        <p class="leads-tag">3 Electrodes – 6 ECG Leads</p>
        <ul>
          <li>No PC or compatibility issues with all hospitals</li>
          <li>Battery life in excess of 72 hours</li>
          <li>Standard alkaline AA batteries</li>
          <li>Single Wi-Fi device</li>
          <li>Simultaneous real-time monitoring and Holter ECG</li>
          <li>Unlimited ECG range in the hospital</li>
        </ul>
      </div>
    </div>
  </article>
</section>

<section class="strip strip--inside" aria-label="Brochure inside">

  <aside class="sidebar">
    <h3 class="sidebar-title">Other Services</h3>
    <ul>
      <li>Outpatient mobile telemetry monitoring</li>
      <li>EKG technician rhythm &amp; software training</li>
    </ul>
    <div class="sidebar-contact">
      <div class="sidebar-title">Contact Information</div>
      Office: (555) 014-2280<br>Toll free: (800) 555-0147<br>Fax: (555) 014-2291
    </div>
  </aside>

  <article class="panel">
    <span class="pill">Contact Information</span>
    <div class="body-copy">
      <p>The below shows the simplicity of 3 electrodes providing six vectors of six ECG leads of the electrical activity of the patient's heart.</p>
      <p>Now: all 12, 3 and 5 channel Holter ECG recorders are obsolete.</p>
      <p>1 and 2 lead patch type Holter ECG recorders are now obsolete.</p>
    </div>
    <span class="pill" style="margin-top:2px">3 Electrodes – 6 Leads</span>
    <div class="chest">
      <div class="figure figure--skin" role="img" aria-label="Torso showing three electrode placement points"></div>
      <div class="lead-list">"EKG"<br>Schema monitoring<br>1 – CM5<br>2 – CM5<br>3 – MV5 (R-modified)<br>4 – MV1<br>5 – MV5<br>6 – aVF</div>
    </div>
  </article>

  <article class="panel panel--alt">
    <h2 class="heading">Anywhere ECG System 100% ECG Telemetry 24/7</h2>
    <div class="figure" style="height:250px;margin-top:10px" role="img" aria-label="Network diagram linking patient transmitters, phones and laptops to the central monitoring station"></div>
  </article>

  <article class="panel">
    <h2 class="heading">Instant Access to Full Disclosure During Real-Time ECG Monitoring</h2>
    <div class="figure figure--screen" style="height:100px;margin-top:6px" role="img" aria-label="Full disclosure ECG monitor screen"></div>
    <ul class="bullets">
      <li>Full disclosure is seen instantly for any patient on the second monitor display.</li>
      <li>Any time period during a 1–30 day study is instantly accessed in full disclosure mode.</li>
      <li>The 24 page scan full disclosure works exactly the same as in Holter.</li>
      <li>Enlarged ECG displays and strips can be viewed and printed at any time.</li>
    </ul>
  </article>

  <article class="panel panel--alt">
    <h2 class="heading">One Click on the V-Tach Trend, and… the Whole Picture of Sustained V-Tach</h2>
    <div class="figure figure--screen" style="height:100px;margin-top:6px" role="img" aria-label="Sustained V-tach ECG trend on monitor"></div>
    <ul class="bullets">
      <li>Monitor 1 continues to show real-time ECG of all patients.</li>
      <li>Monitor 2 shows the V-tach ECG that you probably never get to see.</li>
      <li>And at the end of each month, a Holter ECG file is automatically created on the PC's hard disk for each patient.</li>
    </ul>
  </article>

  <article class="panel">
    <div class="stack">
      <div class="lead-card">
        <div class="band">3-Lead ECG</div>
        <div class="figure" style="height:120px" role="img" aria-label="Three-lead ECG strip"></div>
      </div>
      <div class="lead-card">
        <div class="band">6-Lead ECG</div>
        <div class="figure" style="height:120px" role="img" aria-label="Six-lead ECG strip"></div>
      </div>
    </div>
  </article>

  <article class="panel panel--alt">
    <h2 class="heading">T-Wave Alternans (TWA)</h2>
    <div class="figure" style="height:120px;margin-top:8px" role="img" aria-label="ECG strip showing T-wave alternans"></div>
    <ul class="bullets">
      <li>TWA record is an option and may take 11 years to change outcomes.</li>
      <li>It is included in the Holter processing of each patient.</li>
      <li>Each T wave in each ECG lead is analyzed for the amplitude of the T wave.</li>
      <li>The Holter process takes less than 30 seconds to locate and display the ECG showing TWA.</li>
    </ul>
  </article>
</section>

</body>
</html>
```